iOS7 test prep app

I need 3 basic screens and 2 product images for an iOS7 app I am prototyping. I provided lots of detail in the attached brief. This is an education product, so warm colors (especially reds) work best.

If you've done flat design for mobile products, please take a look ... Thanks!

Greetings, all. Thank you for your submissions. I am meeting with my product development team this week to review your submissions, and will select a designer before the end of the week. I appreciate your patience with my process, and thank you again for your interest in my project. I'll be back to you soon ... -Dorian

```html
<!DOCTYPE html>
<html lang="en">
<head>
<meta charset="utf-8">
<title>Quiz Screens</title>
<link href="https://fonts.googleapis.com/css2?family=Open+Sans:wght@400;600;700&display=swap" rel="stylesheet">
<style>
:root{
  --page:#f3f3f3;
  --red:#d42426;
  --red-halo:#e3e3e3;
  --green:#45a92c;
  --lime:#c3eb6b;
  --tick:#5cb82a;
  --panel:#ebebeb;
  --card:#ffffff;
  --ink:#333333;
  --help:#1d8fc4;
  --orange:#f2541b;
}
*{box-sizing:border-box;margin:0;padding:0}
html,body{width:1024px;height:1200px;overflow:hidden}
body{background:var(--page);font-family:"Open Sans",Arial,sans-serif;color:var(--ink);position:relative}
.screen{position:absolute;top:150px;width:370px;height:838px;background:#fff;overflow:hidden}
.screen--quiz{left:59px}
.screen--answer{left:564px}
.topbar{height:50px;background:var(--red);position:relative;color:#fff;text-align:center;font-weight:700;font-size:15px;line-height:50px}
.menu-icon{position:absolute;left:21px;top:17px;width:29px;height:16px}
.menu-icon span{display:block;height:3px;background:#fff;margin-bottom:3.5px}
.board{position:absolute;top:50px;left:0;width:370px;height:600px;background:var(--panel)}
.question{position:absolute;left:20px;top:35px;width:330px;height:186px;background:var(--card);padding:22px 20px 0 20px;font-size:19px;line-height:30px;color:var(--ink)}
.help-icon{position:absolute;left:168px;top:19px;width:34px;height:34px}
.option{position:absolute;left:20px;width:331px;height:69px}
.option__label{position:absolute;top:0;height:69px;background:var(--card);font-weight:700;font-size:15px;line-height:69px;color:var(--ink);text-transform:uppercase}
.option--left .option__label{left:54px;right:0;padding-left:29px}
.option--right .option__label{left:0;width:262px;padding-left:21px}
.option__badge{position:absolute;top:3px;width:62px;height:62px;border-radius:50%;background:var(--red);color:#fff;font-weight:600;font-size:26px;line-height:62px;text-align:center;box-shadow:0 0 0 6px var(--red-halo)}
.option--left .option__badge{left:0;top:-2px}
.option--right .option__badge{right:0;top:-2px}
.option--correct .option__label{background:var(--lime)}
.option--correct .option__badge{background:var(--lime);color:var(--ink);box-shadow:0 0 0 6px #dfe9cf}
.tick{position:absolute;right:11px;top:24px;width:22px;height:22px}
.footer{position:absolute;top:650px;left:0;width:370px;height:188px;background:#fff}
.count{position:absolute;top:22px;width:100%;text-align:center;color:var(--red);font-weight:700;font-size:15px}
.stop{position:absolute;top:45px;width:40px;height:40px;border-radius:50%;background:#e6e6e6}
.stop span{position:absolute;left:7px;top:7px;width:26px;height:26px;border-radius:50%;color:#fff;font-size:13px;font-weight:700;line-height:26px;text-align:center}
.stop--min{left:19px}.stop--min span{background:var(--red)}
.stop--max{left:310px}.stop--max span{background:var(--green)}
.track{position:absolute;left:77px;top:61px;width:218px;height:8px;border-radius:4px;background:#dcdcdc}
.track__fill{position:absolute;left:0;top:0;width:140px;height:8px;border-radius:4px;background:var(--orange)}
.thumb{position:absolute;left:204px;top:53px;width:24px;height:24px;border-radius:50%;background:#f4f4f4;box-shadow:0 1px 3px rgba(0,0,0,.35)}
.thumb::after{content:"";position:absolute;left:8px;top:8px;width:8px;height:8px;border-radius:50%;background:#d0d0d0}
.explain{position:absolute;left:20px;top:22px;width:335px;font-size:14px;line-height:26px;color:var(--ink)}
.explain strong{font-weight:700}
.btn{position:absolute;top:116px;width:156px;height:46px;color:#fff;font-weight:600;font-size:16px;line-height:46px;text-align:center;text-transform:uppercase}
.btn--red{left:20px;background:var(--red)}
.btn--green{left:195px;background:var(--green)}
</style>
</head>
<body>

<section class="screen screen--quiz">
  <header class="topbar"><div class="menu-icon"><span></span><span></span><span></span></div>QUESTION 7 OF 100</header>
  <div class="board">
    <div class="question">A patient presents to the emergency room with the following symptoms:<br>Anxiety, dyspnea, rhonchi, fever, Oxygen saturation of 88%</div>
    <svg class="help-icon" viewBox="0 0 34 34"><circle cx="17" cy="17" r="16" fill="var(--help)"/><text x="17" y="24" text-anchor="middle" font-family="Open Sans, sans-serif" font-weight="700" font-size="20" fill="#fff">?</text></svg>
    <div class="option option--left" style="top:237px"><div class="option__label">Respiratory Alkalosis</div><div class="option__badge">A</div></div>
    <div class="option option--right" style="top:325px"><div class="option__label">Metabolic Alkalosis</div><div class="option__badge">B</div></div>
    <div class="option option--left" style="top:414px"><div class="option__label">Respiratory Acidosis</div><div class="option__badge">C</div></div>
    <div class="option option--right" style="top:502px"><div class="option__label">Metabolic Acidosis</div><div class="option__badge">D</div></div>
  </div>
  <footer class="footer">
    <div class="count">50 Questions</div>
    <div class="stop stop--min"><span>1</span></div>
    <div class="track"><div class="track__fill"></div></div>
    <div class="thumb"></div>
    <div class="stop stop--max"><span>50</span></div>
    <div class="btn btn--red">Confidence</div>
    <div class="btn btn--green">Submit</div>
  </footer>
</section>

<section class="screen screen--answer">
  <header class="topbar"><div class="menu-icon"><span></span><span></span><span></span></div>QUESTION 7 OF 100</header>
  <div class="board">
    <div class="question">A patient presents to the emergency room with the following symptoms:<br>Anxiety, dyspnea, rhonchi, fever, Oxygen saturation of 88%</div>
    <svg class="help-icon" viewBox="0 0 34 34"><circle cx="17" cy="17" r="16" fill="var(--help)"/><text x="17" y="24" text-anchor="middle" font-family="Open Sans, sans-serif" font-weight="700" font-size="20" fill="#fff">?</text></svg>
    <div class="option option--left" style="top:237px"><div class="option__label">Respiratory Alkalosis</div><div class="option__badge">A</div></div>
    <div class="option option--right" style="top:325px"><div class="option__label">Metabolic Alkalosis</div><div class="option__badge">B</div></div>
    <div class="option option--left option--correct" style="top:414px"><div class="option__label">Respiratory Acidosis
      <svg class="tick" viewBox="0 0 22 22"><circle cx="11" cy="11" r="10" fill="var(--tick)" stroke="#fff" stroke-width="1.5"/><path d="M6.5 11.5l3 3 6-6.5" fill="none" stroke="#fff" stroke-width="2.2" stroke-linecap="round" stroke-linejoin="round"/></svg>
    </div><div class="option__badge">C</div></div>
    <div class="option option--right" style="top:502px"><div class="option__label">Metabolic Acidosis</div><div class="option__badge">D</div></div>
  </div>
  <footer class="footer">
    <p class="explain"><strong>The correct answer is C.</strong> A key symptom of respiratory distress syndrome is the inability of the respiratory system to exchange.</p>
    <div class="btn btn--red">Save &amp; Close</div>
    <div class="btn btn--green">Next Question</div>
  </footer>
</section>

</body>
</html>
```